Revamp our software development company Wix site

We need to rework our Wix website theming, layout, design to match our logo file color and theming. There are a few elements we want to keep, such as the top splash 'typing' header.

The current site is tryheronfield.net. This website I created with Wix, but I never fully finished the copy and all sections.

The feel and mood of the site should be "Warm, professional, inviting, and should project expertise in the field, confidence." But not corporate and cold.

The colors and fonts should match the logo theming. The website must match the logo which was designed in a separate contest. So browns, greens, whites, etc. to create a warm and professional, but fun website.

I want to showcase our app development screenshots in a nice, sharp way.

We are a new company, with only a few clients and projects under our belt. So we don't have lots of need for many testimonials, project showcases, etc. just a couple which is why we went with "Recent work" instead of "Portfolio".

It needs a blog section also that looks great, and will allow me to manage the blog after this project is over. The blog's purpose is for SEO content and marketing.

It will be a huge win for the brieflark artist, to make something unique that doesn't look like every other templated website.

We can use the text/sections found on tryheronfield.net, then i would like to tweak some of the copy and sections later.

***This is a Wix website*** I think it would be 2 pages. The landing page, then the blog page.

***Awesome inspiration websites/vibes we like***
https://brightkestrelstudio.com/
https://vantorel.com/
https://www.quillmeadowcreative.com/
https://www.tesslinworkslab.com/
https://harrow-designco.com/
https://plumtide.studio/

If you have ideas that need to break free from Wix environment, I am open to that idea also. Wix is just easy for a non-technical founder like me to manage our site/blog.

Thanks!

Target Market(s)

Industry leading commercial and residential construction companies seeking custom software development

Industry/Entity Type

We are a boutique software development studio.

Coding

Coded - Design and coding required

Font styles to use
Sans Serif

Requirements
Must have
• Darker/warm background and overall feel. Relaxed and confident vibes. Simplicity, less is more approach. Blog page. Must have project gallery to showcase high res- screenshots. Clear sans serif fonts, nice contrasting colors.
Nice to have
• If it could have some sort of construction related flare, like photos or icon, that could be good, but it cannot be cheesy. A lot of the stock photos of construction workers etc. are terrible and cheesy (please do not use).
Should not have
• lots of pages, music/sounds, busy theming, tiny fonts

```html
<!DOCTYPE html>
<html lang="en">
<head>
<meta charset="utf-8">
<title>Heronfield — Custom Software Studio</title>
<link rel="stylesheet" href="https://fonts.googleapis.com/css2?family=Inter:wght@400;500;600;700&display=swap">
<style>
:root{
  --dark:#393a33;
  --dark-2:#2f302a;
  --lime:#b3c92c;
  --lime-soft:#d6e68f;
  --cream:#fcfaf0;
  --olive:#8a9859;
  --white:#ffffff;
  --text:#2f302a;
  --muted:#5a5b52;
}
*{box-sizing:border-box;margin:0;padding:0}
html,body{width:1200px;height:4360px;overflow:hidden}
body{position:relative;background:var(--cream);font-family:"Inter",Helvetica,Arial,sans-serif;color:var(--text)}
.abs{position:absolute}
.band{position:absolute;left:0;width:1200px}
.brand{font-weight:600;font-size:27px;color:var(--white);display:flex;align-items:center;gap:8px;letter-spacing:-.3px}
.brand-dot{width:14px;height:14px;border-radius:50%;background:var(--lime)}
/* hero */
.hero{top:0;height:750px;background:var(--dark)}
.nav{position:absolute;top:64px;left:457px;display:flex;gap:27px;font-size:13px;color:var(--white)}
.btn{position:absolute;display:flex;align-items:center;justify-content:center;background:var(--lime);color:var(--white);border-radius:22px;font-size:15px}
.hero-title{position:absolute;left:125px;top:250px;font-size:40px;font-weight:600;line-height:59px;color:var(--white)}
.hero-title .accent{color:var(--lime)}
.caret{display:inline-block;width:3px;height:40px;background:var(--lime);vertical-align:-6px;margin-left:4px}
/* intro */
.intro-head{position:absolute;top:830px;left:0;width:1200px;text-align:center;font-size:29px;font-weight:600}
.step{position:absolute;width:440px;height:205px;background:var(--white);border-radius:22px;box-shadow:0 4px 14px rgba(0,0,0,.12);padding:20px 27px}
.step-num{font-size:50px;font-weight:600;color:var(--lime);line-height:1}
.step-name{font-size:19px;font-weight:600;margin-left:12px}
.step p{margin-top:14px;font-size:15px;line-height:19px;color:var(--text)}
/* about */
.about-title{position:absolute;left:546px;top:1620px;font-size:29px;font-weight:600;color:var(--white)}
.acc-line{position:absolute;left:555px;top:1700px;width:2px;height:255px;background:var(--white)}
.acc-item{position:absolute;left:546px;width:530px;font-size:19px;color:var(--white);display:flex;align-items:center}
.acc-item .dot{width:19px;height:19px;border-radius:50%;background:var(--white);margin-right:14px}
.acc-item.open{color:var(--lime);font-weight:600}
.acc-item.open .dot{background:var(--lime)}
.acc-item svg{margin-left:auto}
.acc-body{position:absolute;left:578px;top:1730px;width:460px;font-size:15px;line-height:19px;color:var(--white)}
/* partners */
.badge{position:absolute;top:2165px;width:60px;height:60px;background:#8d8e86}
/* works */
.section-title{position:absolute;left:125px;font-size:29px;font-weight:600;color:var(--text)}
.work-card{position:absolute;top:2438px;width:468px;height:339px;border-radius:22px}
.work-label{position:absolute;left:0;width:100%;text-align:center;font-size:19px;font-weight:600}
/* blogs */
.blog-card{position:absolute;top:3057px;width:374px;height:383px;background:var(--white);border-radius:20px;box-shadow:0 4px 14px rgba(0,0,0,.12);overflow:hidden}
.blog-img{height:251px}
.tags{display:flex;gap:14px;padding:16px 27px 0;white-space:nowrap}
.tag{background:var(--lime-soft);color:var(--muted);font-size:13px;border-radius:14px;padding:5px 16px}
.blog-title{padding:22px 27px 0;font-size:15px;font-weight:600;line-height:19px;color:var(--dark)}
.blog-title.link{text-decoration:underline}
/* contact */
.contact-title{position:absolute;left:205px;top:3658px;font-size:29px;font-weight:600;color:var(--white)}
.contact-copy{position:absolute;left:205px;top:3722px;width:360px;font-size:15px;line-height:18px;color:var(--white)}
.contact-line{position:absolute;left:205px;display:flex;align-items:center;gap:16px;font-size:15px;color:var(--white)}
.field{position:absolute;left:606px;width:387px;height:39px;background:var(--white);border-radius:8px;font-size:12px;color:#9a9a92;padding:12px 14px}
/* footer */
.foot-head{position:absolute;top:4080px;font-size:15px;font-weight:600;letter-spacing:1.5px;color:var(--white);padding-bottom:8px;border-bottom:3px solid var(--lime);width:125px}
.foot-links{position:absolute;top:4124px;font-size:15px;line-height:32px;color:var(--white);list-style:none}
.social{position:absolute;top:4143px;width:22px;height:22px;border-radius:50%;background:var(--white)}
</style>
</head>
<body>

<!-- HERO -->
<section class="band hero">
  <div class="brand abs" style="left:240px;top:56px"><span class="brand-dot"></span>Heronfield</div>
  <nav class="nav"><span>Home</span><span>What We Do</span><span>About Us</span><span>Latest Work</span><span>Blog</span></nav>
  <a class="btn" style="left:855px;top:54px;width:105px;height:41px;font-size:13px;font-weight:600">Contact</a>
  <svg class="abs" style="left:0;top:0" width="1200" height="750" aria-hidden="true">
    <defs>
      <radialGradient id="glow" cx="0" cy="0.7" r="0.4"><stop offset="0" stop-color="#6c7334" stop-opacity=".6"/><stop offset="1" stop-color="#393a33" stop-opacity="0"/></radialGradient>
      <linearGradient id="photoTone" x1="0" y1="0" x2="1" y2="1"><stop offset="0" stop-color="#8c8a6c"/><stop offset=".5" stop-color="#6b5a45"/><stop offset="1" stop-color="#4e4a3a"/></linearGradient>
    </defs>
    <rect width="1200" height="750" fill="url(#glow)"/>
    <path d="M0 640 C300 600 600 700 1200 640" stroke="#4a4b42" fill="none"/>
    <path d="M0 665 C320 625 620 720 1200 665" stroke="#4a4b42" fill="none"/>
  </svg>
  <svg class="abs" style="left:541px;top:152px" width="659" height="510" role="img" aria-label="Photo of a team meeting around a table in a brick-walled office">
    <path d="M160 0 L659 0 L659 510 L40 510 Q0 510 8 470 L120 28 Q128 0 160 0 Z" fill="url(#photoTone)"/>
  </svg>
  <h1 class="hero-title">Take your<br><span class="accent">Client Experience</span><span class="caret"></span><br>to the next level</h1>
  <a class="btn" style="left:125px;top:445px;width:165px;height:51px">Get Started</a>
</section>

<!-- INTRO -->
<h2 class="intro-head">We help leading builders break free from off-the-shelf software.</h2>
<article class="step" style="left:146px;top:920px"><span class="step-num">01</span><span class="step-name">Tailor</span>
  <p>Research shows that less than 10% of software features are frequently used, leaving many bells and whistles unclicked. We'll tailor to fit and eliminate this waste.</p></article>
<article class="step" style="left:612px;top:920px"><span class="step-num">02</span><span class="step-name">Empower</span>
  <p>When your team has tailored tools, they'll work happier, faster, and more effectively towards your goal KPI's. We'll help turn spreadsheets, folder sharing, and emails into streamlined workflows.</p></article>
<article class="step" style="left:146px;top:1152px"><span class="step-num">03</span><span class="step-name">Outcompete</span>
  <p>Deliver results faster, gain performance insights, and leave a lasting impression on clients. Our mission is to create solutions that raise profitability while making your users and clients prefer you over the competition.</p></article>

<!-- ABOUT -->
<svg class="abs" style="left:0;top:1443px" width="1200" height="657" aria-hidden="true">
  <path d="M0 51 L1200 0 L1200 657 L0 657 Z" fill="var(--dark)"/>
</svg>
<svg class="abs" style="left:100px;top:1565px" width="420" height="455" role="img" aria-label="Photo of a team working on laptops around a wooden table">
  <path d="M88 2 L418 2 L418 260 Q418 450 228 450" fill="none" stroke="#b9b9ad" stroke-width="1.5"/>
  <path d="M25 16 L405 16 Q405 452 210 452 L25 452 Z" fill="#7d7262"/>
</svg>
<h2 class="about-title">About Us</h2>
<div class="acc-line"></div>
<div class="acc-item open" style="top:1688px"><span class="dot"></span>OUR STORY
  <svg width="14" height="9" viewBox="0 0 14 9"><path d="M1 8 L7 2 L13 8" stroke="currentColor" stroke-width="2" fill="none"/></svg></div>
<p class="acc-body">At Heronfield, we believe that technology can help businesses achieve more. That's why we've dedicated ourselves to creating software that truly empowers our clients. Our team is made up of experienced developers and business professionals who understand what it takes to succeed in today's competitive landscape.</p>
<div class="acc-item" style="top:1880px"><span class="dot"></span>OUR VISION
  <svg width="14" height="9" viewBox="0 0 14 9"><path d="M1 1 L7 7 L13 1" stroke="currentColor" stroke-width="2" fill="none"/></svg></div>
<div class="acc-item" style="top:1943px"><span class="dot"></span>OUR SOFTWARE
  <svg width="14" height="9" viewBox="0 0 14 9"><path d="M1 1 L7 7 L13 1" stroke="currentColor" stroke-width="2" fill="none"/></svg></div>

<!-- PARTNERS -->
<div class="badge" style="left:139px;border-radius:6px" aria-label="Partner badge"></div>
<div class="badge" style="left:327px;border-radius:50%" aria-label="Partner badge"></div>
<div class="badge" style="left:468px;width:110px;height:44px;top:2173px;border-radius:4px" aria-label="Partner badge"></div>
<div class="badge" style="left:651px;border-radius:50%" aria-label="Partner badge"></div>
<div class="badge" style="left:800px;width:80px;height:40px;top:2175px;background:#c4c4bc;border-radius:4px" aria-label="Partner badge"></div>
<div class="badge" style="left:972px;border-radius:4px" aria-label="Partner badge"></div>

<!-- RECENT WORKS -->
<svg class="abs" style="left:0;top:2289px" width="1200" height="625" aria-hidden="true">
  <path d="M0 0 L1200 0 L1200 571 L0 625 Z" fill="var(--lime-soft)"/>
</svg>
<h2 class="section-title" style="top:2372px">Our Recent Works</h2>
<svg class="abs" style="left:990px;top:2380px" width="80" height="26" aria-hidden="true">
  <path d="M16 3 L7 13 L16 23" stroke="#7d7e75" stroke-width="2.5" fill="none"/>
  <path d="M60 3 L69 13 L60 23" stroke="var(--dark)" stroke-width="2.5" fill="none"/>
</svg>
<article class="work-card" style="left:125px;background:var(--white)">
  <div class="abs" role="img" aria-label="Dashboard screenshot of the TallyDesk ticketing app" style="left:20px;top:65px;width:428px;height:210px;border-radius:10px;background:linear-gradient(160deg,#1f3c53,#15293a);box-shadow:0 6px 14px rgba(0,0,0,.25)"></div>
  <div class="work-label" style="top:296px;color:var(--dark)">TallyDesk</div>
</article>
<article class="work-card" style="left:606px;background:var(--dark)">
  <div class="work-label" style="top:112px;color:var(--white);font-size:25px">Project Title2</div>
  <div class="abs" style="left:150px;top:150px;width:168px;height:3px;background:var(--lime)"></div>
  <p class="abs" style="left:50px;top:185px;width:368px;text-align:center;font-size:12px;line-height:14px;color:var(--white)">Lorem ipsum dolor sit amet consectetur. Augue commodo eu quam sagittis risus magna blandit id lobortis. Amet scelerisque adipiscing id augue sapien a enim. Tincidunt.</p>
  <svg class="abs" style="left:320px;top:250px" width="30" height="44" aria-hidden="true"><path d="M2 2 L2 34 L10 27 L16 42 L22 39 L16 25 L27 25 Z" fill="var(--white)"/></svg>
</article>

<!-- BLOGS -->
<h2 class="section-title" style="top:2995px">Released Blogs</h2>
<article class="blog-card" style="left:125px">
  <div class="blog-img" role="img" aria-label="Photo of a desk with a computer, keyboard and tablet" style="background:linear-gradient(150deg,#8a7866,#5c4a3b)"></div>
  <div class="tags"><span class="tag">#tag1</span><span class="tag">#tag2</span><span class="tag">#tag3</span><span class="tag">#tag4</span><span class="tag">#tag5</span></div>
  <div class="blog-title link">Blog Title, Lorem ipsum dolor sit amet consectetur.</div>
</article>
<article class="blog-card" style="left:526px">
  <div class="blog-img" role="img" aria-label="Photo of a workstation with monitors and a laptop seen from above" style="background:linear-gradient(150deg,#c9c9c4,#8f9291)"></div>
  <div class="tags"><span class="tag">#tag1</span><span class="tag">#tag2</span><span class="tag">#tag3</span><span class="tag">#tag4</span><span class="tag">#tag5</span></div>
  <div class="blog-title">Blog Title, Lorem ipsum dolor sit amet consectetur.</div>
</article>
<article class="blog-card" style="left:927px">
  <div class="blog-img" role="img" aria-label="Photo of a person working on a laptop on a sofa" style="background:linear-gradient(150deg,#d8d2c6,#8e8a80)"></div>
  <div class="tags"><span class="tag">#tag1</span><span class="tag">#tag2</span><span class="tag">#tag3</span><span class="tag">#tag4</span></div>
  <div class="blog-title">Blog Title, Lorem ipsum dolor sit amet consectetur.</div>
</article>
<svg class="abs" style="left:27px;top:3215px" width="39" height="37" aria-hidden="true">
  <rect width="39" height="37" rx="4" fill="#a9aaa2"/><path d="M23 10 L15 18.5 L23 27" stroke="#fff" stroke-width="2.5" fill="none"/>
</svg>
<svg class="abs" style="left:1140px;top:3222px" width="22" height="24" aria-hidden="true"><path d="M7 3 L16 12 L7 21" stroke="#fff" stroke-width="2.5" fill="none"/></svg>

<!-- CONTACT -->
<div class="band" style="top:3550px;height:470px;background:var(--dark)"></div>
<h2 class="contact-title">Ready to talk?</h2>
<p class="contact-copy">You can share some quick info by this form and we'll reach out. You can also contact us directly via:</p>
<div class="contact-line" style="top:3794px">
  <svg width="22" height="16" aria-hidden="true"><rect x="1" y="1" width="20" height="14" rx="2" fill="#fff"/><path d="M2 2 L11 9 L20 2" stroke="var(--dark)" stroke-width="1.6" fill="none"/></svg>marcus@tryheronfield.net</div>
<div class="contact-line" style="top:3833px">
  <svg width="22" height="20" viewBox="0 0 24 24" aria-hidden="true"><path d="M6.6 10.8a15 15 0 0 0 6.6 6.6l2.2-2.2c.3-.3.7-.4 1-.2 1.1.4 2.3.6 3.6.6.6 0 1 .4 1 1V20c0 .6-.4 1-1 1A17 17 0 0 1 3 4c0-.6.4-1 1-1h3.5c.6 0 1 .4 1 1 0 1.3.2 2.5.6 3.6.1.3 0 .7-.2 1z" fill="#fff"/></svg>903.555.0187</div>
<div class="field" style="top:3636px">Name</div>
<div class="field" style="top:3684px">Type of work interested with</div>
<div class="field" style="top:3733px">Email</div>
<div class="field" style="top:3780px">Phone</div>
<a class="btn" style="left:606px;top:3836px;width:105px;height:42px;border-radius:8px">Submit</a>

<!-- FOOTER -->
<svg class="abs" style="left:0;top:3964px" width="1200" height="396" aria-hidden="true">
  <path d="M0 51 L1200 0 L1200 396 L0 396 Z" fill="var(--olive)"/>
</svg>
<div class="brand abs" style="left:291px;top:4080px;font-size:30px"><span class="brand-dot"></span>Heronfield</div>
<span class="social" style="left:293px" aria-label="Social profile"></span>
<span class="social" style="left:345px" aria-label="Social profile"></span>
<span class="social" style="left:398px" aria-label="Social profile"></span>
<div class="foot-head" style="left:506px">NAVIGATION</div>
<ul class="foot-links" style="left:506px"><li>Home</li><li>What We Do</li><li>Abous Us</li><li>Latest Work</li><li>Blog</li><li>Contact</li></ul>
<div class="foot-head" style="left:707px">INFORMATION</div>
<div class="contact-line" style="left:707px;top:4124px;gap:10px"><svg width="16" height="12" aria-hidden="true"><rect width="16" height="12" rx="2" fill="#fff"/><path d="M1 1 L8 7 L15 1" stroke="var(--olive)" stroke-width="1.4" fill="none"/></svg>marcus@tryheronfield.net</div>
<div class="contact-line" style="left:707px;top:4156px;gap:10px"><svg width="16" height="16" viewBox="0 0 24 24" aria-hidden="true"><path d="M6.6 10.8a15 15 0 0 0 6.6 6.6l2.2-2.2c.3-.3.7-.4 1-.2 1.1.4 2.3.6 3.6.6.6 0 1 .4 1 1V20c0 .6-.4 1-1 1A17 17 0 0 1 3 4c0-.6.4-1 1-1h3.5c.6 0 1 .4 1 1 0 1.3.2 2.5.6 3.6.1.3 0 .7-.2 1z" fill="#fff"/></svg>903-555-0187</div>
<div class="contact-line" style="left:707px;top:4190px;gap:10px;align-items:flex-start;line-height:19px"><svg width="16" height="20" viewBox="0 0 16 20" aria-hidden="true"><path d="M8 0a7 7 0 0 0-7 7c0 5 7 13 7 13s7-8 7-13a7 7 0 0 0-7-7zm0 10a3 3 0 1 1 0-6 3 3 0 0 1 0 6z" fill="#fff"/></svg><span>1820 Larkspur Ct.<br>Fort Worth, TX 76100</span></div>

</body>
</html>
```